Baby Led Weaning App complete design

I want to develop a new app and I need full design for it, including screens, toolbars, icons, images, logo,etc.
The app is aiming to show the User information about baby led weaning, with theory and guidelines and it should also contain a section with recipes for baby lead weaning.

Industry/Entity Type
Baby
Requirements
Must have
- Full design for the app, including screens, toolbars, icons, images, logo,etc.
- The app will be used on smartphones and tablets so design should consider different screen sizes.

Nice to have
- The app is mainly for mums with babys. The design should be bright, happy (positive) and easy to use.
- It would be good to have nice images of babys feeding themselves (no bottle milk). The images in the documents provided need to be replaced.
- Colurs should be gender neutral (not specific to girl or boy).

Should not have
- The should not look too serious or cold.
- Nothing that can be interpreted as negative, heavy, complicated or sad.

```html
<!DOCTYPE html>
<html lang="en">
<head>
<meta charset="UTF-8">
<title>Baby Led Weaning – Onboarding</title>
<link rel="stylesheet" href="https://fonts.googleapis.com/css2?family=Montserrat:wght@600;700&family=Roboto:wght@300;400&display=swap">
<style>
  :root {
    --backdrop: #efeeee;
    --screen: #f8f8f9;
    --sunny: #f0e45c;
    --white: #ffffff;
    --ink: #1b1b1f;
    --muted: #a9a9ad;
    --pink: #f584a1;
    --dot-ring: #2a2a2e;
  }
  * { margin: 0; padding: 0; box-sizing: border-box; }
  html, body {
    width: 1200px; height: 744px; overflow: hidden;
    background: var(--backdrop);
  }
  .canvas {
    position: relative; width: 1200px; height: 744px;
  }
  .screen {
    position: absolute; left: 410px; top: 34px;
    width: 380px; height: 676px;
    background: var(--screen);
    overflow: hidden;
    box-shadow: 0 10px 40px rgba(0,0,0,0.08);
  }
  .hero-band {
    position: absolute; left: 0; top: 0; width: 380px; height: 440px;
  }
  .brand-badge {
    position: absolute; left: 105px; top: 92px;
    width: 170px; height: 150px; border-radius: 50%;
    background: var(--white);
  }
  .brand-name {
    position: absolute; left: 0; top: 262px; width: 380px;
    text-align: center;
    font-family: "Montserrat", sans-serif; font-weight: 700;
    font-size: 27px; line-height: 31px; color: var(--white);
  }
  .intro {
    position: absolute; left: 24px; top: 470px; width: 332px;
  }
  .intro-title {
    font-family: "Montserrat", sans-serif; font-weight: 600;
    font-size: 19px; color: var(--ink); margin-bottom: 8px;
  }
  .intro-text {
    font-family: "Roboto", sans-serif; font-weight: 400;
    font-size: 12px; line-height: 16px; color: var(--muted);
  }
  .pager {
    position: absolute; left: 0; top: 568px; width: 380px;
    display: flex; justify-content: center; gap: 7px;
  }
  .pager-dot {
    width: 11px; height: 11px; border-radius: 50%;
    border: 1.5px solid var(--dot-ring);
  }
  .pager-dot.is-active { background: var(--pink); border-color: var(--pink); }
  .cta {
    position: absolute; left: 24px; top: 598px;
    width: 332px; height: 54px; border-radius: 4px;
    background: var(--pink); color: var(--white);
    font-family: "Roboto", sans-serif; font-weight: 300; font-size: 18px;
    display: flex; align-items: center; justify-content: center;
  }
</style>
</head>
<body>
<div class="canvas">
  <div class="screen">
    <svg class="hero-band" viewBox="0 0 380 440" aria-hidden="true">
      <path d="M0 0 H380 V395 Q250 400 170 440 L0 440 Z" fill="var(--sunny)"/>
    </svg>
    <div class="brand-badge" role="img" aria-label="App emblem: spoon and fork"></div>
    <div class="brand-name">Baby Led<br>Weaning</div>

    <section class="intro">
      <h1 class="intro-title">Guidelines for baby led wearing</h1>
      <p class="intro-text">Lorem ipsum dolor sit amet, consectetur adipisicing elit, sed do eiusmod tempor incididunt ut labore et</p>
    </section>

    <div class="pager">
      <span class="pager-dot is-active"></span>
      <span class="pager-dot"></span>
      <span class="pager-dot"></span>
    </div>

    <div class="cta">Get Started</div>
  </div>
</div>
</body>
</html>
```